Welcome to the neighborhood

We need two post card designs for Marsh and Fern Insurance Company.

The first one is when someone moves into a new home.
We want it to include the following:

Congratulations and welcome to the neighborhood.
We are a local independent insurance agency established in 1912
Please let us know if we can be of service to you.

Second post card to send after 6 months in the area should include the following:

Just to let you know................

Marsh and Fern Insurance Agency was established over 100 years ago.
We are in the neighborhood and would appreciate the opportunity to provide you with a no obligation insurance review.
We will offer multiple quotes from several A rated insurance companies and will give you a $10.00 Brewlark gift card to quote your home and auto insurance.
We have saved hundreds of dollars for our clients by offering more coverage at a lower premium.
Please let our professional staff help you with your insurance needs.

Target Market(s)

Individuals that own a home and cars

Industry/Entity Type

Insurance

Font styles to use
Serif

Requirements
Must have
• Marsh and Fern Logo - we have it on jpg file - we tried to attach it but it doesn't seem like it worked
Our colors are black and gold - please incorporate these colors on the postcard
Website www.marshandfern-example.com
Like us on Chatterly
Agency address and phone number
417 Quillon Avenue Suite 318
Harrowmere, ZN 60987
(555)555-0142
Nice to have
• Some visual appeal relative to the topic - home and car - people - somethinng creative

```html
<!DOCTYPE html>
<html lang="en">
<head>
<meta charset="utf-8">
<title>Marsh and Fern Insurance Agency – Postcard</title>
<link rel="stylesheet" href="https://fonts.googleapis.com/css2?family=Cinzel:wght@400;600&family=Open+Sans:ital,wght@1,400&display=swap">
<style>
  :root {
    --ink: #000000;
    --panel: #080808;
    --gold: #c9a23a;
    --gold-deep: #a97e2a;
    --gold-bright: #e6c45a;
    --white: #ffffff;
  }
  html, body {
    margin: 0;
    padding: 0;
    width: 1200px;
    height: 930px;
    overflow: hidden;
    background: var(--ink);
  }
  .postcard {
    position: relative;
    width: 1200px;
    height: 930px;
    background: radial-gradient(ellipse at 50% 35%, #151515 0%, var(--panel) 55%, var(--ink) 100%);
    font-family: "Cinzel", "Trajan Pro", serif;
    color: var(--gold);
  }
  .brand-name {
    position: absolute;
    top: 78px;
    left: 0;
    width: 1200px;
    text-align: center;
    font-family: "Cinzel", serif;
    font-weight: 400;
    font-size: 74px;
    line-height: 100px;
    color: var(--gold);
    margin: 0;
  }
  .brand-tagline {
    position: absolute;
    top: 214px;
    left: 0;
    width: 1200px;
    text-align: center;
    font-family: "Open Sans", Arial, sans-serif;
    font-style: italic;
    font-size: 70px;
    line-height: 88px;
    color: var(--white);
    margin: 0;
  }
  .message {
    position: absolute;
    left: 0;
    width: 1200px;
    text-align: center;
    margin: 0;
    font-size: 30px;
    line-height: 26px;
    white-space: nowrap;
    color: var(--gold);
  }
  .message span { display: block; }
  .message-intro { top: 344px; font-size: 31px; color: var(--gold-deep); }
  .message-history { top: 395px; line-height: 25px; }
  .message-offer { top: 470px; }
  .message-savings { top: 596px; line-height: 27px; }
  .message-savings span:first-child,
  .message-savings span:last-child { color: var(--gold-bright); }
  .divider {
    position: absolute;
    top: 738px;
    left: 53px;
    width: 1094px;
    height: 3px;
    background: var(--gold);
  }
  .contact {
    position: absolute;
    margin: 0;
    color: var(--white);
    font-size: 24px;
    line-height: 38px;
    white-space: nowrap;
  }
  .contact span { display: block; }
  .contact-online { top: 804px; left: 55px; }
  .contact-office { top: 790px; right: 55px; text-align: right; line-height: 29px; font-size: 24px; }
</style>
</head>
<body>
  <main class="postcard">
    <h1 class="brand-name">Marsh and Fern</h1>
    <p class="brand-tagline">Insurance Agency, Inc.</p>

    <p class="message message-intro"><span>Just to let you know...</span></p>
    <p class="message message-history">
      <span>Marsh and Fern Insurance Agency was established over 100 years ago.</span>
      <span>We are in the neighborhood and would appreciate the opportunity</span>
    </p>
    <p class="message message-offer">
      <span>to provide you with a no obligation insurance review.</span>
      <span>We will offer multiple quotes from several A rated insurance</span>
      <span>companies and will give you a $10.00 Brewlark gift card to quote</span>
      <span>your home and auto insurance.</span>
    </p>
    <p class="message message-savings">
      <span>We have saved hundreds of dollars for our clients by offering</span>
      <span>more coverage at a lower premium.</span>
      <span>Please let our professional staff help you with your insurance needs.</span>
    </p>

    <div class="divider"></div>

    <p class="contact contact-online">
      <span>Like us on Chatterly</span>
      <span>www.marshandfern-example.com</span>
    </p>
    <p class="contact contact-office">
      <span>417 Quillon Avenue Suite 318</span>
      <span>Harrowmere, ZN 60987</span>
      <span>(555)555-0142</span>
    </p>
  </main>
</body>
</html>
```